Naturopath Practitioner Card Design

I am a naturopath needing a design for a business card mainly to show that I am a naturopath and have some contact details to give to prospective clients. I am open minded about the design and what is on the second side of the card whether it just be some artwork or space for details, appointment times etc. Naturopathy is the practice of natural medicine that uses a holistic approach and incorporates herbal and nutritional medicine.

Industry/Entity Type

Business

Contact Information for Business Card

Tom Welby NaturopathBHSc (Naturopathy) Member PHRA 0492 815 306 tom.welby@mailbright.com www.tomwelbynaturopathy.com.au

Requirements
Nice to have
• Would prefer some kind of original pattern/art work/logo rather than an image, not fussed if its very simple/basic
• I am open to any colour but think I would prefer a more earthy sandy clay etc type style than the greens that are commonly associated with naturopathy.
Should not have
• Don't really want to have generic stock images on it

```html
<!DOCTYPE html>
<html lang="en">
<head>
<meta charset="utf-8">
<title>Tom Welby Naturopathy – Business Card</title>
<link rel="stylesheet" href="https://fonts.googleapis.com/css2?family=Open+Sans:wght@400;600;700&display=swap">
<style>
  :root {
    --page-bg: #ece8e3;
    --card-bg: #ffffff;
    --leaf-green: #6b8a2e;
    --ink: #333333;
    --rule: #555555;
    --card-shadow: rgba(0, 0, 0, 0.18);
  }
  * { box-sizing: border-box; margin: 0; padding: 0; }
  html, body {
    width: 1200px;
    height: 1000px;
    overflow: hidden;
    background: var(--page-bg);
    font-family: "Open Sans", Arial, sans-serif;
    color: var(--ink);
  }
  .canvas { position: relative; width: 1200px; height: 1000px; }
  .card {
    position: absolute;
    left: 265px;
    width: 666px;
    height: 397px;
    background: var(--card-bg);
    box-shadow: 0 6px 14px var(--card-shadow);
  }
  .card--front { top: 73px; }
  .card--back { top: 533px; }

  /* Brand name: one line, one colour, one weight, plain circle beside */
  .brand {
    position: absolute;
    display: flex;
    align-items: center;
    gap: 14px;
    font-family: "Open Sans", Arial, sans-serif;
    font-weight: 400;
    color: var(--ink);
    white-space: nowrap;
    line-height: 1;
  }
  .brand__dot {
    flex: none;
    border-radius: 50%;
    background: var(--leaf-green);
  }
  .card--front .brand { left: 33px; top: 150px; font-size: 32px; }
  .card--front .brand__dot { width: 40px; height: 40px; }
  .card--back .brand { right: 32px; top: 108px; font-size: 26px; }
  .card--back .brand__dot { width: 32px; height: 32px; }

  .practitioner {
    position: absolute;
    right: 32px;
    top: 227px;
    text-align: right;
  }
  .practitioner__name {
    font-size: 23px;
    font-weight: 600;
    color: var(--leaf-green);
    line-height: 1.15;
  }
  .practitioner__name small { font-size: 17px; font-weight: 400; }
  .practitioner__role { font-size: 18px; line-height: 1.3; }
  .divider {
    position: absolute;
    left: 33px;
    top: 268px;
    width: 478px;
    height: 2px;
    background: linear-gradient(to right, rgba(85,85,85,0), var(--rule) 60%, var(--rule));
  }
  .contact-list {
    position: absolute;
    left: 33px;
    top: 296px;
    list-style: none;
    font-size: 17px;
  }
  .contact-list li { display: flex; align-items: center; height: 25.5px; }
  .contact-list svg { width: 14px; height: 14px; margin-right: 9px; fill: var(--leaf-green); }

  /* Back */
  .appointment-title {
    position: absolute;
    left: 33px;
    top: 116px;
    font-size: 18px;
    font-weight: 700;
    color: var(--leaf-green);
  }
  .field {
    position: absolute;
    left: 33px;
    width: 601px;
    font-size: 16px;
    border-bottom: 1.5px solid var(--rule);
    padding-bottom: 2px;
  }
  .field--date { top: 198px; }
  .field--time { top: 249px; }
  .day-row {
    position: absolute;
    left: 33px;
    top: 304px;
    width: 601px;
    display: flex;
    justify-content: space-between;
    font-size: 16px;
  }
  .day { display: flex; align-items: center; }
  .day__box {
    width: 15px; height: 15px;
    border: 2px solid var(--leaf-green);
    margin-left: 10px;
  }
  .notice {
    position: absolute;
    left: 33px;
    top: 346px;
    font-size: 17px;
  }
</style>
</head>
<body>
<main class="canvas">

  <section class="card card--front" aria-label="Business card front">
    <div class="brand">
      <span class="brand__dot" aria-hidden="true"></span>
      <span class="brand__name">Tom Welby Naturopathy</span>
    </div>

    <div class="practitioner">
      <p class="practitioner__name">TOM WELBY <small>BHSc</small></p>
      <p class="practitioner__role">Naturopathy</p>
    </div>
    <div class="divider"></div>

    <ul class="contact-list">
      <li>
        <svg viewBox="0 0 16 16" aria-hidden="true"><path d="M2 6c0-2 3-3 6-3s6 1 6 3v1h-3V5.5H5V7H2zM4 8h8l2 5H2z"/></svg>
        0492 815 306
      </li>
      <li>
        <svg viewBox="0 0 16 16" aria-hidden="true"><path d="M1 3h14v10H1z M1 3l7 5 7-5" stroke="#fff" stroke-width="1.2"/></svg>
        tom.welby@mailbright.com
      </li>
      <li>
        <svg viewBox="0 0 16 16" aria-hidden="true"><circle cx="8" cy="8" r="7"/><path d="M5 4c2 0 3 2 2 3s-2 1-1 3M10 10c1-1 2 0 3-1" stroke="#fff" stroke-width="1.2" fill="none"/></svg>
        www.tomwelbynaturopathy.com.au
      </li>
    </ul>
  </section>

  <section class="card card--back" aria-label="Business card back, appointment card">
    <h2 class="appointment-title">APPOINTMENT</h2>
    <div class="brand">
      <span class="brand__dot" aria-hidden="true"></span>
      <span class="brand__name">Tom Welby Naturopathy</span>
    </div>

    <p class="field field--date">Date:</p>
    <p class="field field--time">Time:</p>

    <div class="day-row">
      <span class="day">MON<span class="day__box"></span></span>
      <span class="day">TUE<span class="day__box"></span></span>
      <span class="day">WED<span class="day__box"></span></span>
      <span class="day">THUR<span class="day__box"></span></span>
      <span class="day">FRI<span class="day__box"></span></span>
      <span class="day">SAT<span class="day__box"></span></span>
    </div>

    <p class="notice">If you are unable to keep your appointment , please allow 24 hours notice</p>
  </section>

</main>
</body>
</html>
```